Modern and Sleek Non-Fiction Book Cover Design

Seeking a talented graphic designer to create a modern and sleek cover and back page for a book to be published on Pagewick . The design should be visually appealing and align with the book's theme, using bright colors to make it stand out. The title is "The Counsel Office Welcome Manual" with "The" in a smaller font, and the tagline "Intake as a Competitive Advantage" should be included. The book is targeted at an audience interested in immigration and family law firms. So I would like it on the cover as well. The hex numbers for the colors are 00aeeef, fcb034, and 336a89. The cover should feature the author's photo prominently.
-Design a modern front cover for the book
-Design a sleek back page for the book
-Ensure designs meet Pagewick publishing requirements 8x5 paperback
Let's not use the side image, it doesn't seem to fit like I thought it might.

```html
<!DOCTYPE html>
<html lang="en">
<head>
<meta charset="utf-8">
<title>The Counsel Office Welcome Manual</title>
<link rel="stylesheet" href="https://fonts.googleapis.com/css2?family=Inter:wght@500;600;800&family=Source+Serif+4:ital,wght@1,400&display=swap">
<style>
  :root {
    --cream: #f7f7ea;
    --ink: #0d0d0d;
    --serif-blue: #4a6aa8;
    --sky: #1f9bd7;
    --sky-deep: #1680c0;
    --slate: #6f6f70;
    --sun: #fcc014;
    --white: #ffffff;
  }
  html, body {
    margin: 0;
    padding: 0;
    width: 1200px;
    height: 900px;
    overflow: hidden;
    background: var(--cream);
  }
  .cover {
    position: relative;
    width: 1200px;
    height: 900px;
    display: grid;
    grid-template-columns: 776px 424px;
  }
  .title-panel {
    background: var(--cream);
    position: relative;
  }
  .title-block {
    position: absolute;
    left: 110px;
    top: 206px;
  }
  .title-lead {
    font-family: "Source Serif 4", Georgia, serif;
    font-style: italic;
    font-weight: 400;
    color: var(--serif-blue);
    font-size: 58px;
    line-height: 1;
    margin: 0 0 6px;
  }
  .title-main {
    font-family: "Inter", Arial, sans-serif;
    font-weight: 800;
    color: var(--ink);
    font-size: 96px;
    line-height: 0.97;
    letter-spacing: -2px;
    margin: 0;
  }
  .title-main span { display: block; }
  .subtitle {
    font-family: "Source Serif 4", Georgia, serif;
    font-style: italic;
    color: var(--serif-blue);
    font-size: 42px;
    line-height: 1;
    margin: 14px 0 0;
  }
  .side-column {
    display: grid;
    grid-template-rows: 434px 195px 271px;
  }
  .author-photo {
    background: linear-gradient(160deg, var(--sky) 0%, var(--sky-deep) 100%);
  }
  .tagline-band {
    background: var(--slate);
    display: flex;
    align-items: center;
    justify-content: center;
    text-align: center;
    padding: 0 40px;
    font-family: "Inter", Arial, sans-serif;
    font-weight: 500;
    font-size: 28px;
    line-height: 1.25;
    color: var(--white);
  }
  .audience-band {
    background: var(--sun);
    display: flex;
    align-items: center;
    justify-content: center;
    text-align: center;
    font-family: "Inter", Arial, sans-serif;
    font-weight: 600;
    font-size: 23px;
    line-height: 1.25;
    color: var(--ink);
  }
</style>
</head>
<body>
  <main class="cover">
    <section class="title-panel">
      <div class="title-block">
        <p class="title-lead">The</p>
        <h1 class="title-main">
          <span>Counsel</span>
          <span>Office</span>
          <span>Welcome</span>
          <span>Manual</span>
        </h1>
        <p class="subtitle">&amp; Marketing Guide</p>
      </div>
    </section>
    <aside class="side-column">
      <div class="author-photo" role="img" aria-label="Author portrait photograph on a bright blue background"></div>
      <p class="tagline-band" style="margin:0">Intake as a<br>Competitive Advantage</p>
      <div class="audience-band">For Immigration<br>and Family Law<br>law firms</div>
    </aside>
  </main>
</body>
</html>
```